Business Card Design

We need a business card designed for a new company based in Melbourne called KPo solutions. KPo solutions provides management consulting specialising in the health and social services sector.

KPo solutions offer a unique set of specialist skills │dealing with all levels of government │ unique communication skills│intimate knowledge of the health sector │solutions tailored to unique circumstances.

KPo solutions takes on a select number of clients at any one time, this ensures that your organisation receives the attention required. On larger projects, KPo solutions join up with other consultants to bring specialist skills to a project.
Updates

This is the first time I have used Pattern Hive and thank you all for responding. The variation is amazing and makes it hard to decide. I have to ask some of my friends to give me their views. The response is fantastic. The one I pick will basically be the most visually appealing

Industry/Entity Type

Management Consulting

Contact Information for Business Card

Martin Hollis, Principal, KPo solutions, 14 Calloway Ave, Westbridge VIC 3094, 0438 712 304, martinh@kposolutions.com.au, www.kposolutions.com.au

```html
<!DOCTYPE html>
<html lang="en">
<head>
<meta charset="utf-8">
<title>KPo solutions – Business Card</title>
<link href="https://fonts.googleapis.com/css2?family=Arimo:ital,wght@0,400;0,700;1,700&display=swap" rel="stylesheet">
<style>
  :root {
    --backdrop: #e6e2dc;
    --brand-red: #c00010;
    --band-black: #000000;
    --paper-white: #ffffff;
    --ink: #111111;
  }
  html, body {
    margin: 0;
    padding: 0;
    width: 1200px;
    height: 798px;
    overflow: hidden;
    background: var(--backdrop);
    font-family: "Arimo", Arial, sans-serif;
  }
  .business-card {
    position: absolute;
    left: 107px;
    top: 94px;
    width: 986px;
    height: 608px;
    background: var(--paper-white);
    box-shadow: 0 6px 18px rgba(0,0,0,0.18);
  }
  .brand-panel {
    position: absolute;
    left: 0; top: 0;
    width: 100%;
    height: 428px;
    background: var(--brand-red);
  }
  .divider-band {
    position: absolute;
    left: 0; top: 428px;
    width: 100%;
    height: 11px;
    background: var(--band-black);
  }
  .footer-band {
    position: absolute;
    left: 0; bottom: 0;
    width: 100%;
    height: 10px;
    background: var(--band-black);
  }
  .brand-name {
    position: absolute;
    left: 137px;
    top: 116px;
    margin: 0;
    font-size: 56px;
    font-weight: 400;
    line-height: 1;
    letter-spacing: 1px;
    color: var(--paper-white);
  }
  .brand-tagline {
    position: absolute;
    left: 197px;
    top: 201px;
    margin: 0;
    font-size: 14px;
    font-weight: 700;
    letter-spacing: 0.6px;
    color: var(--paper-white);
  }
  .person {
    position: absolute;
    right: 58px;
    top: 357px;
    text-align: right;
  }
  .person-name {
    margin: 0;
    font-size: 29px;
    font-weight: 400;
    letter-spacing: 1.5px;
    line-height: 1;
    color: var(--paper-white);
    word-spacing: 5px;
  }
  .person-role {
    margin: 6px 0 0;
    font-size: 24px;
    font-weight: 700;
    font-style: italic;
    line-height: 1;
    color: var(--band-black);
  }
  .contact {
    position: absolute;
    right: 58px;
    top: 486px;
    margin: 0;
    text-align: right;
    font-style: normal;
    font-size: 17px;
    line-height: 23px;
    letter-spacing: 0.4px;
    word-spacing: 3px;
    color: var(--ink);
  }
</style>
</head>
<body>
  <article class="business-card">
    <div class="brand-panel"></div>
    <div class="divider-band"></div>
    <div class="footer-band"></div>

    <h1 class="brand-name">KPo solutions</h1>
    <p class="brand-tagline">HEALTH &amp; SOCIAL SERVICES CONSULTING</p>

    <div class="person">
      <p class="person-name">MARTIN HOLLIS</p>
      <p class="person-role">Principal</p>
    </div>

    <address class="contact">
      14 Calloway Ave. Westbridge VIC 3094<br>
      T: 0438 712 304 E: martinh@kposolutions.com.au W: www.kposolutions.com
    </address>
  </article>
</body>
</html>
```